Stationary for decorative plumbing and hardware showroom
Fine Home Fittings
Professional
Wendell Okafor
2417 Morrow Parkway
Suite 420
Houston, TX 77091
wendell@lumivessa.com
www.lumivessa.com

```html
<!DOCTYPE html>
<html lang="en">
<head>
<meta charset="utf-8">
<title>LumiVessa Stationery</title>
<link href="https://fonts.googleapis.com/css2?family=Raleway:wght@400;500&display=swap" rel="stylesheet">
<style>
  :root{
    --backdrop:#dcdddf;
    --paper:#ffffff;
    --ink:#1a1a1a;
    --band:#151515;
    --swoosh:#8c8c8c;
    --muted:#6b6b6b;
    --body-text:#444444;
    --rule:#d0d0d0;
    --text-font:"Raleway", Arial, sans-serif;
  }
  *{box-sizing:border-box;margin:0;padding:0}
  html,body{width:1200px;height:936px;overflow:hidden}
  body{background:var(--backdrop);position:relative;font-family:var(--text-font);color:var(--ink)}
  .sheet{position:absolute;background:var(--paper);overflow:hidden;box-shadow:0 2px 6px rgba(0,0,0,.18)}
  .wave{position:absolute;left:0;bottom:0;width:100%;display:block}
  .brand{font-family:var(--text-font);font-weight:500;letter-spacing:.08em;color:var(--ink);display:flex;align-items:center;gap:.35em;line-height:1;white-space:nowrap}
  .brand-dot{width:.3em;height:.3em;background:var(--ink);border-radius:50%}

  /* Letterhead */
  .letterhead{left:173px;top:51px;width:423px;height:614px}
  .letterhead .brand{position:absolute;left:34px;top:42px;font-size:21px}
  .letterhead .contact{position:absolute;right:30px;top:38px;font-size:6px;line-height:1.6;color:var(--muted)}
  .letter-body{position:absolute;left:34px;top:112px;width:345px;font-size:5.6px;line-height:1.65;color:var(--body-text)}
  .letter-body p{margin-bottom:9px}
  .letter-body .sign{margin-top:26px}
  .letterhead .wave{height:250px}

  /* Folder */
  .folder{left:634px;top:38px;width:482px;height:629px}
  .folder .brand{position:absolute;left:0;right:0;top:182px;justify-content:center;font-size:42px}
  .folder .wave{height:240px}

  /* Business cards */
  .card{width:203px;height:77px}
  .card-front{left:46px;top:715px}
  .card-front .brand{position:absolute;left:14px;top:14px;font-size:12px}
  .card-front .contact{position:absolute;right:12px;top:12px;font-size:4.6px;line-height:1.5;color:var(--muted)}
  .card-front .wave{height:26px}
  .card-back{left:46px;top:825px;display:flex;align-items:center;justify-content:center}
  .card-back .web{font-size:9px;letter-spacing:.35em;color:var(--ink)}

  /* Envelopes */
  .envelope{width:444px;height:203px}
  .envelope-front{left:279px;top:710px}
  .envelope-front .brand{position:absolute;left:26px;top:26px;font-size:21px}
  .envelope-front .address{position:absolute;left:26px;top:58px;font-size:6.5px;line-height:1.55;color:var(--muted)}
  .envelope-back{left:761px;top:710px;width:393px}
  .envelope-back .flap{position:absolute;left:0;top:0;width:100%;height:100%}
  .envelope-back .web{position:absolute;left:0;right:0;top:36px;text-align:center;font-size:10px;letter-spacing:.4em;color:var(--paper)}
</style>
</head>
<body>

<section class="sheet letterhead">
  <div class="brand">LUMIVESSA<span class="brand-dot"></span></div>
  <div class="contact">
    2417 Morrow Parkway, Suite 420<br>
    Houston, TX 77091<br>
    wendell@lumivessa.com<br>
    www.lumivessa.com
  </div>
  <div class="letter-body">
    <p>July 7, 2025</p>
    <p>Dear Client,<br>4410 Garden Row, Houston, TX</p>
    <p>Thank you for visiting our showroom. Our team has gathered a wide range of fine faucets, sinks, tubs and cabinet hardware for every room in your home. We look forward to helping you choose pieces that suit your style and last for years.</p>
    <p>Each fitting in our collection is selected for its finish, craft and lasting quality. Our staff will gladly arrange samples and quotes at your convenience.</p>
    <p>Please call or write to set up a private visit. We are open six days a week and happy to meet with builders, designers and home owners alike.</p>
    <p>Best Regards,</p>
    <p class="sign">Wendell Okafor<br>Director</p>
  </div>
  <svg class="wave" viewBox="0 0 400 200" preserveAspectRatio="none" aria-hidden="true">
    <path d="M0,70 C120,10 270,15 400,35 L400,200 L0,200Z" fill="var(--swoosh)"/>
    <path d="M0,112 C130,45 270,50 400,62 L400,200 L0,200Z" fill="var(--paper)"/>
    <path d="M0,120 C130,55 270,58 400,70 L400,200 L0,200Z" fill="var(--band)"/>
  </svg>
</section>

<section class="sheet folder">
  <div class="brand">LUMIVESSA<span class="brand-dot"></span></div>
  <svg class="wave" viewBox="0 0 400 200" preserveAspectRatio="none" aria-hidden="true">
    <path d="M0,55 C120,5 270,10 400,30 L400,200 L0,200Z" fill="var(--swoosh)"/>
    <path d="M0,100 C130,40 270,45 400,58 L400,200 L0,200Z" fill="var(--paper)"/>
    <path d="M0,108 C130,50 270,54 400,66 L400,200 L0,200Z" fill="var(--band)"/>
  </svg>
</section>

<section class="sheet card card-front">
  <div class="brand">LUMIVESSA<span class="brand-dot"></span></div>
  <div class="contact">
    Wendell Okafor<br>
    2417 Morrow Parkway, Suite 420<br>
    Houston, TX 77091<br>
    wendell@lumivessa.com
  </div>
  <svg class="wave" viewBox="0 0 400 100" preserveAspectRatio="none" aria-hidden="true">
    <path d="M0,40 C130,0 270,10 400,20 L400,100 L0,100Z" fill="var(--swoosh)"/>
    <path d="M0,62 C130,25 270,30 400,38 L400,100 L0,100Z" fill="var(--band)"/>
  </svg>
</section>

<section class="sheet card card-back">
  <div class="web">www.LumiVessa.com</div>
</section>

<section class="sheet envelope envelope-front">
  <div class="brand">LUMIVESSA<span class="brand-dot"></span></div>
  <div class="address">
    2417 Morrow Parkway, Suite 420<br>
    Houston, TX 77091
  </div>
</section>

<section class="sheet envelope envelope-back">
  <svg class="flap" viewBox="0 0 393 203" preserveAspectRatio="none" aria-hidden="true">
    <path d="M0,0 L393,0 L393,70 C300,130 93,130 0,70Z" fill="var(--band)"/>
    <path d="M0,70 C93,130 300,130 393,70" fill="none" stroke="var(--rule)" stroke-width="1"/>
  </svg>
  <div class="web">www.LumiVessa.com</div>
</section>

</body>
</html>
```